Flyer-Design für Internethandel auf ausgewählten Marktplätzen
Zielgruppe
Internethandel auf Marktplätzen wie: Verkano, Lumo, Fiska.de, Brix.de
Eigene Webseite: www.talbrunn-laden.de
So ganz festgelegt habe ich mch noch nicht was ich alles im Sortiment haben möchte.
Im Moment besteht der Hauptteil aus Pflaster verschiedenster Sorten, aus verschiedenen Klebebandsorten und aus Werkzeugen wie Cuttermesser und passende Klingen.
Aufgabenstellung
Ich möchte (mit den Farben des Logos ?) einen Flyer, um Käufer darum zu bitten eine bewertung für mich abzugeben.
Soetwas wie: wir sind stets bemüht unsere Service-Leistungen zu verbessern und freuen uns, wenn Sie diese mit einer positven Bewertung honorieren. Siehe angehängtes Bild, das habe ich heute von einem anderen verkäufer bekommen.
Sehr gerne auch einen anderen passenden Text.
Was ich auch gerne hätte, wäre der Hinweis auf unsere Webseite www.talbrunn-laden.de
Dort bieten wir auch Staffelpreise an und Käufer können dadurch sparen wenn Sie mehr kaufen.
Ich habe mal zwei Bilder von Klebebänder mit angehängt. Eventuell können Sie ja auf unserer Internetseite ein Passendes Bild von Klebebandrollen, Pflaster oder Arbeitsschutzmaterial kopieren.
Es ist aber kein muss ein Bild mit ein zu setzen.
Bedruckt werden sollten beide seiten. Größe: Ca. Postkartengröße?!

```html
<!DOCTYPE html>
<html lang="de">
<head>
<meta charset="utf-8">
<title>Talbrunn-Laden – Bewertungskarte</title>
<link rel="stylesheet" href="https://fonts.googleapis.com/css2?family=Great+Vibes&family=Mulish:wght@300;400;800&display=swap">
<style>
  :root {
    --page-bg: #c6c6c6;
    --card-bg: #ffffff;
    --text: #5a5a5a;
    --text-dark: #4a4a4a;
    --brand-green: #4db848;
    --band-green: #8aab2c;
    --band-blue: #1f4e79;
    --band-yellow: #f5d000;
    --star: #f6c012;
    --star-edge: #d99a00;
    --smile: #2ecc2e;
  }
  * { margin: 0; padding: 0; box-sizing: border-box; }
  html, body { width: 1109px; height: 1200px; overflow: hidden; }
  body {
    background: var(--page-bg);
    position: relative;
    font-family: "Mulish", sans-serif;
    color: var(--text);
  }
  .card {
    position: absolute;
    width: 646px;
    height: 455px;
    background: var(--card-bg);
    overflow: hidden;
  }
  .card--front { left: 102px; top: 115px; }
  .card--back  { left: 334px; top: 630px; }

  .brand {
    position: absolute;
    display: flex;
    align-items: center;
    gap: 6px;
    font-family: "Mulish", sans-serif;
    font-weight: 400;
    font-size: 15px;
    color: #6b6b6b;
    white-space: nowrap;
  }
  .brand__dot { width: 9px; height: 9px; border-radius: 50%; background: var(--brand-green); }

  /* front */
  .greeting {
    position: absolute; left: 96px; top: 42px;
    font-family: "Great Vibes", cursive;
    font-size: 34px; color: var(--text-dark);
  }
  .card--front .brand { left: 486px; top: 70px; }
  .intro, .request {
    position: absolute; left: 96px;
    font-size: 13.2px; line-height: 20px; font-weight: 400;
  }
  .intro { top: 103px; width: 400px; }
  .request { top: 262px; width: 360px; }
  .stars { position: absolute; left: 96px; top: 195px; display: flex; gap: 0; }
  .thumbs-photo {
    position: absolute; left: 90px; top: 326px; width: 470px; height: 129px;
    background: linear-gradient(180deg, #ffffff 0%, #f2d3bd 45%, #d9a07e 80%, #9c6645 100%);
  }

  /* back */
  .banner-photo {
    position: absolute; left: 4px; top: 0; width: 640px; height: 132px;
    background: linear-gradient(90deg, #e9e9e9 0%, #d7dde3 40%, #e6e6e6 70%, #ececec 100%);
  }
  .banner-band { position: absolute; left: 4px; top: 132px; width: 640px; height: 12px; display: flex; }
  .banner-band span:nth-child(1) { width: 208px; background: var(--band-green); }
  .banner-band span:nth-child(2) { width: 228px; background: var(--band-blue); }
  .banner-band span:nth-child(3) { flex: 1; background: var(--band-yellow); }
  .banner-label {
    position: absolute; font-size: 10.5px; font-weight: 300; color: #3e3e3e; letter-spacing: 0.1px;
  }
  .banner-label--firstaid { left: 35px; top: 55px; }
  .banner-label--household { left: 386px; top: 25px; }
  .banner-label--diy { left: 354px; top: 73px; }

  .headline {
    position: absolute; left: 47px; top: 160px;
    font-size: 15px; line-height: 22px; font-weight: 800; color: var(--brand-green);
  }
  .card--back .brand { left: 454px; top: 190px; }
  .benefit { position: absolute; top: 236px; width: 180px; }
  .benefit--gift { left: 41px; }
  .benefit--volume { left: 228px; }
  .benefit--shipping { left: 415px; }
  .benefit__head { display: flex; gap: 10px; align-items: flex-start; }
  .benefit__icon { flex: 0 0 25px; height: 25px; border-radius: 50%; background: var(--smile); border: 1.5px solid #1a7a1a; }
  .benefit__title { font-size: 13px; font-weight: 800; color: var(--text-dark); line-height: 20px; padding-top: 3px; }
  .benefit__text { margin: 6px 0 0 6px; font-size: 13.2px; line-height: 20px; font-weight: 400; }
  .cta {
    position: absolute; left: 403px; top: 384px; width: 186px; height: 36px;
    border-radius: 18px; background: var(--brand-green);
    color: #fff; font-size: 12.5px; font-weight: 400;
    display: flex; align-items: center; justify-content: center; text-decoration: none;
  }
</style>
</head>
<body>

<section class="card card--front">
  <h1 class="greeting">Liebe Kunden,</h1>
  <div class="brand"><span class="brand__dot"></span>Talbrunn-Laden</div>
  <p class="intro">herzlichen Dank für Ihre Bestellung und Ihr Vertrauen!<br>Unser Bestreben ist es, Ihnen nicht nur einwandfreie Produkte und Leistungen anzubieten, sondern auch unseren Service stets zu verbessern.</p>
  <svg class="stars" width="192" height="42" viewBox="0 0 192 42" aria-label="Fünf Sterne">
    <defs>
      <polygon id="star" points="19,2 24,14 37,15 27,24 30,37 19,30 8,37 11,24 1,15 14,14" fill="var(--star)" stroke="var(--star-edge)" stroke-width="1.2" stroke-linejoin="round"/>
    </defs>
    <use href="#star" x="0"/><use href="#star" x="38"/><use href="#star" x="76"/><use href="#star" x="114"/><use href="#star" x="152"/>
  </svg>
  <p class="request">Hierzu benötigen wir Ihr Feedack und freuen uns über<br>&nbsp;Ihre Bewertung – danke!</p>
  <div class="thumbs-photo" role="img" aria-label="Foto: viele erhobene Hände mit Daumen hoch"></div>
</section>

<section class="card card--back">
  <div class="banner-photo" role="img" aria-label="Foto: Erste-Hilfe-Koffer mit Sportlerin, zwei Heimwerker mit Bohrmaschinen und Werkzeugkasten, zwei Personen mit Putzmitteln"></div>
  <div class="banner-band"><span></span><span></span><span></span></div>
  <span class="banner-label banner-label--firstaid">ERSTE HILFE</span>
  <span class="banner-label banner-label--household">Haushaltsartikel</span>
  <span class="banner-label banner-label--diy">Heimwerkerbedarf</span>

  <h2 class="headline">Ihr Online-Shop für Verbandstoffe, Wundversorgung<br>Haushalts- und Heimwerkerbedarf</h2>
  <div class="brand"><span class="brand__dot"></span>Talbrunn-Laden</div>

  <div class="benefit benefit--gift">
    <div class="benefit__head"><span class="benefit__icon"></span><h3 class="benefit__title">Gratis-Geschenk</h3></div>
    <p class="benefit__text">Ein Einkauf bei uns lohnt sich immer, denn zu den unschlagbar günstigen Preisen erhalten Sie bei Ihrem Einkauf ab 15 € ein Gratis-Geschenk.</p>
  </div>
  <div class="benefit benefit--volume">
    <div class="benefit__head"><span class="benefit__icon"></span><h3 class="benefit__title">Mengenrabatte</h3></div>
    <p class="benefit__text">Ab 3 Stück bekommen Sie bei uns schon einen attrak­tiven Mengenrabatt. Kombi­nation mit gleichwertigen Artikeln möglich.</p>
  </div>
  <div class="benefit benefit--shipping">
    <div class="benefit__head"><span class="benefit__icon"></span><h3 class="benefit__title">Sparen Sie sich die Versandkosten</h3></div>
    <p class="benefit__text">Ab 75 Euro Warenwert über­nehmen wir die Versand­kosten innerhalb Deutsch­land für Sie.</p>
  </div>

  <a class="cta" href="#">www.talbrunn-laden.de</a>
</section>

</body>
</html>
```